Portrait Photographer Newsletter (www.lakesidelensworks.com)

We would like a newsletter that can be used in Mailbright Hub....you can visit our website to get some content....The main topics for the newsletter are 1. planning for your family portraits 2. We also offer restoration of your family heirlooms 3. Coming Soon.....www.dockandcottageguard.com (get content off our website.)
Misc:
Gift Certificates are available.
Click to schedule you appt today.
Mothers day.
I can provide more pictures but we really need the content of the news letter- we need a good writer...feel free to use info our of our website or be creative :)
We need help keeping up with email marketing if we find a fit, we would like to use find someone to help with this weekly or monthly
Target Market(s)
Family, middle to upper class
Industry/Entity Type
Portrait Photography
Designer to choose colors to be used in the design.

```html
<!DOCTYPE html>
<html lang="en">
<head>
<meta charset="utf-8">
<title>Lakeside Lensworks Newsletter</title>
<link rel="stylesheet" href="https://fonts.googleapis.com/css2?family=Libre+Baskerville:wght@400;700&family=Open+Sans:wght@400;600;700&display=swap">
<style>
  :root {
    --sky: #a9d4ec;
    --brand-blue: #2a9be0;
    --navy: #222456;
    --ink: #1e2040;
    --text: #5a5a5a;
    --page: #ffffff;
    --stage: #e9ecef;
    --sand: #d9c2a0;
    --sea: #4f86b4;
  }
  * { box-sizing: border-box; margin: 0; padding: 0; }
  html, body { width: 1200px; height: 762px; overflow: hidden; }
  body { background: var(--stage); font-family: "Open Sans", sans-serif; position: relative; }

  .newsletter {
    position: absolute; left: 428px; top: 10px;
    width: 420px; height: 905px;
    background: var(--page);
    transform: scale(0.82); transform-origin: top left;
    box-shadow: 0 4px 14px rgba(0,0,0,.18);
  }
  .masthead { height: 68px; background: var(--sky); text-align: center; padding-top: 12px; }
  .brand-name { font-family: "Libre Baskerville", serif; font-size: 19px; color: var(--ink); }
  .brand-name::before { content: ""; display: inline-block; width: 8px; height: 8px; background: var(--ink); border-radius: 50%; margin-right: 7px; vertical-align: middle; }
  .brand-tagline { font-size: 5px; letter-spacing: 1px; color: var(--ink); margin-top: 4px; }

  .headline-band {
    height: 50px; background: var(--brand-blue); color: #fff;
    font-family: "Libre Baskerville", serif; font-size: 14.5px; line-height: 17px;
    text-align: center; padding: 8px 12px 0;
  }
  .hero-photo { display: block; height: 194px; background: linear-gradient(to bottom, #b8d6ee 0%, var(--sea) 30%, #8fb3cc 48%, var(--sand) 60%, #cdb48e 100%); box-shadow: 0 8px 10px -6px rgba(0,0,0,.25); }

  .planning { display: flex; padding: 32px 14px 0 18px; gap: 14px; }
  .planning-copy { width: 200px; }
  .section-title { font-family: "Libre Baskerville", serif; font-weight: 700; font-size: 15.5px; line-height: 16px; color: var(--ink); }
  .body-copy { font-size: 8.4px; line-height: 12px; color: var(--text); text-align: justify; margin-top: 8px; }
  .body-copy + .body-copy { margin-top: 4px; }
  .house-frame { width: 174px; height: 154px; border: 1px solid var(--ink); padding: 4px; margin-top: 0; }
  .house-photo { width: 100%; height: 100%; background: linear-gradient(to bottom, #5d8fc4 0%, #9cc0de 40%, #3c4a63 58%, #4e7d3a 78%, #b5a994 100%); }

  .gallery { position: absolute; left: 18px; top: 527px; width: 386px; height: 160px; }
  .gallery > * { position: absolute; }
  .photo-baby { left: 0; top: 0; width: 114px; height: 160px; background: linear-gradient(to bottom, #9dbbd6 0%, #c9d5dd 35%, #d8c6a7 70%, #2f8fd0 100%); }
  .photo-girls { left: 118px; top: 0; width: 96px; height: 160px; background: linear-gradient(to bottom, #b4cddf 0%, #9ca88b 40%, #3c3d5a 70%, #d4c2a2 100%); }
  .photo-jump { left: 218px; top: 0; width: 82px; height: 77px; background: linear-gradient(to bottom, #a7cbe5 0%, #8bb4d0 50%, #dcc9a8 100%); }
  .photo-lighthouse { left: 304px; top: 0; width: 82px; height: 77px; background: linear-gradient(135deg, #a43a2e 0%, #d4d0c8 60%, #b03a30 100%); }
  .offer-box { left: 218px; top: 82px; width: 168px; height: 78px; background: var(--navy); color: #fff; text-align: center; font-size: 12px; line-height: 15px; padding-top: 16px; }
  .offer-box strong { font-weight: 700; display: block; }

  .perks { position: absolute; left: 0; top: 693px; width: 420px; height: 106px; background: var(--brand-blue); display: flex; justify-content: space-around; padding: 14px 20px 0; }
  .perk { width: 110px; text-align: center; color: #fff; font-size: 10px; line-height: 12px; }
  .perk-icon { width: 46px; height: 46px; border-radius: 50%; background: #fff; margin: 0 auto 8px; display: flex; align-items: center; justify-content: center; }

  .schedule { position: absolute; left: 0; top: 817px; width: 420px; text-align: center; }
  .schedule-title { font-family: "Libre Baskerville", serif; font-size: 19px; color: var(--brand-blue); letter-spacing: .5px; }
  .schedule-copy { font-size: 9.8px; line-height: 12px; color: var(--text); margin-top: 5px; padding: 0 24px; }
  .contact-line { display: flex; justify-content: space-between; padding: 0 18px; margin-top: 16px; font-size: 8.6px; color: #333; }
  .contact-line span { display: flex; align-items: center; gap: 3px; }
</style>
</head>
<body>
<main class="newsletter">
  <header class="masthead">
    <div class="brand-name">Lakeside Lensworks</div>
    <div class="brand-tagline">ARTISTIC PORTRAITS. FAMILY HEIRLOOMS</div>
  </header>
  <div class="headline-band">Trust Dock &amp; Cottage Guard will keep a careful eye on your property!</div>
  <div class="hero-photo" role="img" aria-label="Family of six holding hands walking along the beach by the sea"></div>

  <section class="planning">
    <div class="planning-copy">
      <h2 class="section-title">PLANNING FOR YOUR FAMILY PORTRAITS</h2>
      <p class="body-copy">Lorem ipsum dolor sit amet, consectetur adipiscing elit, sed do eiusmod tempor incididunt ut labore et dolore magna aliqua. Ut enim ad mi</p>
      <p class="body-copy">quis nostrud exercitation ullamco laboris nisi ut aliquip ex ea commodo consequat. Duis aute irure dolor in reprehenderit in voluptate velit esse cillum dolore eu fugiat nulla pariatur. Excepteur sint occaecat cupidatat non ui officia deserunt mollit anim id est laborum.</p>
    </div>
    <div class="house-frame"><div class="house-photo" role="img" aria-label="Large beach house with lit windows at dusk"></div></div>
  </section>

  <section class="gallery">
    <div class="photo-baby" role="img" aria-label="Toddler on the beach with a blue birthday cake"></div>
    <div class="photo-girls" role="img" aria-label="Two sisters in striped dresses among dune grass"></div>
    <div class="photo-jump" role="img" aria-label="Group jumping on the beach"></div>
    <div class="photo-lighthouse" role="img" aria-label="Family beside a red and white buoy"></div>
    <div class="offer-box"><strong>WE ALSO OFFER</strong>RESTORATION OF YOUR FAMILY HEIRLOOMS</div>
  </section>

  <section class="perks">
    <div class="perk">
      <div class="perk-icon"><svg width="22" height="22" viewBox="0 0 22 22"><rect x="3" y="8" width="16" height="12" fill="var(--navy)"/><rect x="2" y="5" width="18" height="4" fill="var(--navy)"/><rect x="10" y="5" width="2" height="15" fill="#fff"/><path d="M11 5 C7 0 4 3 8 5 M11 5 C15 0 18 3 14 5" stroke="var(--navy)" stroke-width="1.6" fill="none"/></svg></div>
      Gift Certificates<br>are available.
    </div>
    <div class="perk">
      <div class="perk-icon"><svg width="22" height="22" viewBox="0 0 22 22"><rect x="2" y="4" width="17" height="15" rx="1.5" fill="none" stroke="var(--navy)" stroke-width="1.8"/><rect x="2" y="4" width="17" height="4" fill="var(--navy)"/><rect x="6" y="1.5" width="2" height="4" fill="var(--navy)"/><rect x="13" y="1.5" width="2" height="4" fill="var(--navy)"/><circle cx="17" cy="17" r="4.5" fill="var(--navy)"/><path d="M15 17 l1.5 1.5 l2.5 -3" stroke="#fff" stroke-width="1.3" fill="none"/></svg></div>
      Click to schedule<br>you appt today
    </div>
    <div class="perk">
      <div class="perk-icon"><svg width="22" height="22" viewBox="0 0 22 22"><path d="M11 19 C3 13 1 9 3.5 5.5 C6 2.5 9.5 4 11 6.5 C12.5 4 16 2.5 18.5 5.5 C21 9 19 13 11 19 Z" fill="var(--navy)"/></svg></div>
      Mothers day
    </div>
  </section>

  <section class="schedule">
    <h2 class="schedule-title">SCHEDULE AN APPOINTMENT</h2>
    <p class="schedule-copy">with us to learn about how we can protect your beach home while you are away- our new business:</p>
    <div class="contact-line">
      <span><svg width="7" height="9" viewBox="0 0 7 9"><path d="M3.5 9 C1 5.5 0 4.5 0 3.5 A3.5 3.5 0 0 1 7 3.5 C7 4.5 6 5.5 3.5 9 Z" fill="#333"/><circle cx="3.5" cy="3.4" r="1.2" fill="#fff"/></svg>Harbor Point, Maine</span>
      <span><svg width="8" height="8" viewBox="0 0 8 8"><circle cx="4" cy="4" r="3.6" fill="#777"/></svg>www.dockandcottageguard.com</span>
      <span><svg width="10" height="8" viewBox="0 0 10 8"><path d="M1 3 C3 0 7 0 9 3 L7.5 4 L6.5 2.8 L3.5 2.8 L2.5 4 Z" fill="#333"/><rect x="2" y="4.2" width="6" height="3.5" rx=".6" fill="#333"/></svg>555-014-2290</span>
    </div>
  </section>
</main>
</body>
</html>
```